Massage Clinic needs a Flyer for Advertising

Our massage clinic, 'Keel Line Massage Therapy', has recently opened in Osborne Park, Western Australia. We are specialists in deep tissue and sports massage. We also offer relaxation, trigger point therapy, stretching techniques, and postural and functional movement analysis. We're based within the same building complex as a personal training and Ironvane box. There are also a number of local gyms in the area. Our target clients are both the local athletes, but also local business (Osborne Park is a business district in Perth).

We need double-sided DL size flyer. We would like the design to incorporate the colouring of the logo (green, purple, grey), but happy for it to use anything that enhances this also. Logo has been attached (.png and .ai format). There is also a selection of photos available to use if required, other stylised images would also be accepted. We'd like the flyer to include business details, services, and price list (price list is optional). We can provide further descriptions of key therapies on offer if required for inclusion.

Target Market(s)

Local athletes (gym, Ironvane, sport), and local business employees.

Industry/Entity Type

Massage Therapy

Font styles to use
Sans Serif

Requirements
Must have
• List of Services to be included:
• Relaxation Massage
• Deep Tissue Massage
• Sports Massage
• Neuromuscular (Trigger Point) Therapy
• Postural Analysis
• Musculoskeletal and Functional Movement Screening
• Therapeutic Stretching (including Proprioceptive Neuromuscular Facilitation and Muscle Energy Technique)
• All sessions are customised to suit the needs of the client, and may incorporate a variety of the above techniques.
• Business location and Contact details:
• 4/18 Tamsin Road, Osborne Park WA 6017
• Phone: 0417 362 804
• Email: info@keelline.net.au
Nice to have
• Symbols for showing the company has Facebook and Instagram accounts.
• The business is also a member of GPRV - logo attached below, please include.
• Price details are shown in one of the attached images, and copied below:
• Individual -
• 30 minutes $45
• 60 minutes $85
• Packages -
• 4 x 30 minutes $165
• 4 x 60 minutes $305
• (Packages valid for two months; pre-payment required).
Should not have
• Please don't use any imagery/design that looks suited to a day-spa environment. My massage clinic is located within a gym environment.
• If you use stock photo's, please select one where the therapists hands are female (both are stuff are currently female therapists).

```html
<!DOCTYPE html>
<html lang="en">
<head>
<meta charset="utf-8">
<title>Keel Line Massage Therapy – Treatment Options</title>
<link rel="stylesheet" href="https://fonts.googleapis.com/css2?family=Montserrat:wght@400;500;600;700&display=swap">
<style>
  :root {
    --brand-purple: #6b2c91;
    --brand-green: #8cb83f;
    --brand-grey: #646464;
    --ink: #1f1f1f;
    --paper: #ffffff;
    --skin-light: #e7c2a6;
    --skin-mid: #c99476;
    --skin-deep: #9a6a50;
    --towel: #f4f1ee;
  }
  * { margin: 0; padding: 0; box-sizing: border-box; }
  html, body { width: 1200px; height: 2546px; overflow: hidden; background: var(--paper); }
  body { font-family: "Montserrat", Arial, sans-serif; color: var(--ink); }

  .flyer { position: relative; width: 1200px; height: 2546px; background: var(--paper); }

  .brand {
    position: absolute; left: 130px; top: 150px; width: 940px; height: 260px;
    display: flex; align-items: center; gap: 44px;
  }
  .brand-dot { flex: none; width: 70px; height: 70px; border-radius: 50%; background: var(--brand-green); }
  .brand-name {
    font-weight: 600; color: var(--brand-purple);
    font-size: 84px; line-height: 1.05; letter-spacing: -1px;
  }

  .hero-photo {
    position: absolute; left: 0; top: 517px; width: 1200px; height: 576px;
    background:
      linear-gradient(180deg, var(--towel) 0%, var(--towel) 14%, rgba(244,241,238,0) 30%),
      radial-gradient(ellipse 60% 55% at 55% 60%, var(--skin-light) 0%, var(--skin-mid) 55%, var(--skin-deep) 100%);
  }

  .treatments { position: absolute; left: 0; top: 1190px; width: 1200px; text-align: center; }
  .treatments-title {
    font-weight: 700; color: var(--brand-green);
    font-size: 58px; letter-spacing: 1px; line-height: 1;
  }
  .treatments-intro {
    margin: 40px auto 0; width: 960px;
    font-size: 35px; font-weight: 400; line-height: 1.36; color: var(--ink);
  }
  .service-list { list-style: none; margin-top: 44px; }
  .service {
    font-weight: 700; color: var(--brand-purple);
    font-size: 43px; letter-spacing: 1px; line-height: 1.3;
    margin-bottom: 46px;
  }
  .service-note {
    display: block; font-weight: 400; color: var(--ink);
    font-size: 33px; letter-spacing: 0; line-height: 1.35; margin-top: 2px;
  }
  .service:last-child { margin-bottom: 0; }
</style>
</head>
<body>
  <main class="flyer">
    <header class="brand">
      <span class="brand-dot"></span>
      <div class="brand-name">Keel Line<br>Massage Therapy</div>
    </header>

    <div class="hero-photo" role="img" aria-label="Photo of a female therapist's hands massaging a client's lower back, white towel above"></div>

    <section class="treatments">
      <h1 class="treatments-title">TREATMENT OPTIONS</h1>
      <p class="treatments-intro">All sessions are customised to suit the needs of the client, and may incorporate a variety of the techniques listed below.</p>
      <ul class="service-list">
        <li class="service">RELAXATION MASSAGE</li>
        <li class="service">DEEP TISSUE MASSAGE</li>
        <li class="service">SPORTS MASSAGE</li>
        <li class="service">NEUROMUSCULAR<br>(TRIGGER POINT) THERAPY</li>
        <li class="service">POSTURAL ANALYSIS</li>
        <li class="service">MUSCULOSKELETAL AND<br>FUNCTIONAL MOVEMENT<br>SCREENING</li>
        <li class="service">THERAPEUTIC STRETCHING
          <span class="service-note">Includes Proprioceptive Neuromuscular Facilitation<br>and Muscle Energy Technique.</span>
        </li>
      </ul>
    </section>
  </main>
</body>
</html>
```